international electric export business, needs help us Wordpress PSD design

we need a web page design, we are manufacturer and exporter of electric and electronic goods in China, for our products, you can visit our website: www.tolvirex.com, now we would like to improve the page of tolvirex.com, in order to get more attractive, We would like that it is simple and lookds confortable.
So we would like you to help us WORDPRESS PSD.
Target Market(s)
We are the factory and manufacture the low, medium and high voltage electric products, major export to South America, Middle East, Europe countries.
Our products used in construction and industry, similar Korvath, DLQ
Our customers are wholeseller, not retailer or end user.
Industry/Entity Type
Electronic
Font styles to use
Colors
Designer to choose colors to be used in the design.
Look and feel
Each slider illustrates characteristics of the customer's brand and the style your logo design should communicate.

```html
<!DOCTYPE html>
<html lang="en">
<head>
<meta charset="utf-8">
<title>Tolvirex Electric</title>
<link href="https://fonts.googleapis.com/css2?family=Source+Sans+3:wght@300;400;600&family=Alegreya:ital,wght@1,700&display=swap" rel="stylesheet">
<style>
:root{
  --red:#c8000a;
  --red-dark:#a30008;
  --red-light:#e0151b;
  --ink:#333;
  --muted:#777;
  --line:#dcdcdc;
  --panel:#f4f4f4;
  --dark-btn:#2b2b2b;
}
*{box-sizing:border-box;margin:0;padding:0}
html,body{width:874px;height:1200px;overflow:hidden;background:#fff}
body{position:relative;font-family:"Source Sans 3",Arial,sans-serif;color:var(--ink);font-weight:300}
.abs{position:absolute}
.top-strip{left:0;top:0;width:874px;height:5px;background:#ececec}

.brand{left:90px;top:30px;display:flex;align-items:center;gap:8px}
.brand-mark{width:14px;height:14px;background:var(--red)}
.brand-name{font-size:22px;font-weight:600;color:var(--red)}
.brand-sep{width:1px;height:28px;background:#ccc;margin:0 6px}
.tagline{font-family:"Alegreya",serif;font-style:italic;font-weight:700;font-size:19px;color:#8a8a8a}

.search{left:530px;top:53px;width:175px;height:22px;border:1px solid var(--line);font-size:9px;color:#999;font-style:italic;padding:5px 8px}
.search svg{position:absolute;right:6px;top:4px}
.lang{left:715px;top:53px;width:74px;height:22px;border:1px solid var(--line);font-size:10px;font-weight:400;padding:4px 6px;display:flex;align-items:center;gap:5px}
.flag{width:14px;height:9px;background:#23408e;position:relative}
.flag::before{content:"";position:absolute;left:0;top:3.5px;width:14px;height:2px;background:#d8222a}

.nav{left:83px;top:86px;width:708px;height:36px;background:linear-gradient(#e0151b,#b8000a);border-radius:3px 3px 0 0;display:flex;padding-left:2px}
.nav a{color:#fff;text-decoration:none;font-size:13.5px;font-weight:400;padding:0 16px;line-height:36px;border-right:1px solid rgba(0,0,0,.2);box-shadow:1px 0 0 rgba(255,255,255,.15)}
.nav a.current{padding:0 22px 0 26px}

.slider{left:83px;top:122px;width:708px;height:255px;border:1px solid var(--line);border-top:0;background:linear-gradient(#fff 40%,#eee);border-radius:0 0 3px 3px}
.slide-title{left:42px;top:57px;font-size:30px;font-weight:300;color:#222}
.slide-text{left:43px;top:95px;width:290px;font-size:10.5px;line-height:17.5px;color:#333}
.btn-dark{background:var(--dark-btn);color:#fff;font-size:9.5px;font-weight:400;border-radius:3px;text-align:center}
.slide-btn{left:43px;top:155px;width:78px;height:24px;line-height:24px}
.slide-photo{left:370px;top:30px;width:320px;height:190px;border-radius:8px;background:radial-gradient(ellipse at 50% 55%,#dcdcdc,#f2f2f2 60%,rgba(255,255,255,0) 75%)}
.dots{left:328px;top:228px;display:flex;gap:4px}
.dots span{width:10px;height:10px;border-radius:50%;background:#aaa}
.dots span:first-child{background:#666}

.teaser{top:389px;width:231px;height:124px;border:1px solid var(--line);background:linear-gradient(#fff,#f6f6f6)}
.teaser h3{position:absolute;left:16px;top:11px;font-size:15.5px;font-weight:400;color:var(--red)}
.teaser .thumb{position:absolute;left:16px;top:37px;width:66px;height:66px;border:1px solid #ddd}
.teaser p{position:absolute;left:92px;top:35px;width:130px;font-size:8.5px;line-height:14px;color:#666}
.teaser .btn-dark{position:absolute;left:92px;top:84px;width:62px;height:20px;line-height:20px;font-size:7.5px;font-weight:600}

.side{left:83px;top:535px;width:172px;height:222px;border:1px solid var(--line);background:#fff}
.side-head{height:32px;background:linear-gradient(#f4f4f4,#e6e6e6);border-bottom:1px solid var(--line);font-size:15px;font-weight:400;padding:7px 17px;color:#333}
.side ul{list-style:none;padding:8px 12px 0 18px}
.side li{font-size:9.5px;line-height:21px;border-bottom:1px solid #e4e4e4;padding-left:12px;position:relative;color:#444}
.side li:last-child{border-bottom:0}
.side li::before{content:"";position:absolute;left:2px;top:8px;border-left:3px solid #999;border-top:3px solid transparent;border-bottom:3px solid transparent}

.recommend{left:269px;top:535px;width:521px;height:222px;border:1px solid var(--line)}
.rec-head{height:38px;background:linear-gradient(#d50f15,#b4000a);color:#fff;font-size:17px;font-weight:400;padding:9px 18px;border-radius:3px 3px 0 0}
.rec-grid{display:flex;height:183px}
.product{flex:1;border-right:1px solid var(--line);padding:10px 0 0 22px;position:relative;background:linear-gradient(#fff,#f8f8f8)}
.product:last-child{border-right:0}
.product .pic{width:87px;height:76px;border:1px solid #ddd;background:linear-gradient(135deg,#f5f5f5,#c9c9c9)}
.product h4{font-size:10px;font-weight:400;margin-top:8px;color:#222}
.product p{font-size:7.5px;line-height:12.5px;color:#666;width:100px;margin-top:2px}
.btn-red{position:absolute;left:22px;top:154px;width:57px;height:17px;line-height:17px;background:var(--red);color:#fff;font-size:7px;font-weight:600;text-align:center;border-radius:2px}

.about{left:84px;top:783px;width:472px}
.about h2{font-size:19px;font-weight:300;color:#222;margin-bottom:8px}
.about p{font-size:9px;line-height:16.5px;color:#333;margin-bottom:7px}

.chat{left:573px;top:781px;width:217px;height:136px;border:1px solid var(--line);background:#fff}
.chat h3{position:absolute;left:16px;top:13px;font-size:17px;font-weight:300;line-height:20px;color:var(--red)}
.chat p{position:absolute;left:16px;top:58px;width:86px;font-size:7.5px;line-height:12px;color:#999}
.chat .btn-dark{position:absolute;left:16px;top:103px;width:48px;height:16px;line-height:16px;font-size:6.5px;border-radius:9px}
.chat .photo{position:absolute;right:0;top:20px;width:112px;height:115px;background:linear-gradient(#f7f2ee,#e8ddd4)}

.footer{left:0;top:960px;width:874px;height:190px;background:linear-gradient(#eee,#fff 30px)}
.fcol{position:absolute;top:28px;height:118px;border-right:1px solid #e2e2e2}
.fcol h5{font-size:14px;font-weight:400;color:var(--red);margin-bottom:7px}
.fcol li{list-style:none;font-size:9.5px;line-height:19.5px;color:#333;display:flex;align-items:center;gap:6px}
.skype{width:12px;height:12px;border-radius:50%;background:#1aa3e0}
.social{display:flex;gap:6px;margin-top:2px}
.social span{width:17px;height:17px;border-radius:2px}
.copyright{left:0;top:1150px;width:874px;border-top:1px solid #e4e4e4;padding:13px 0 0 86px;font-size:8.5px;color:#777}
</style>
</head>
<body>
<div class="abs top-strip"></div>

<header>
  <div class="abs brand">
    <span class="brand-mark"></span><span class="brand-name">Tolvirex</span>
    <span class="brand-sep"></span>
    <span class="tagline">Science and techno reform the life.</span>
  </div>
  <div class="abs search">Search here..
    <svg width="12" height="12" viewBox="0 0 12 12"><circle cx="5" cy="5" r="3.8" fill="none" stroke="#555" stroke-width="1.6"/><line x1="8" y1="8" x2="11" y2="11" stroke="#555" stroke-width="1.8"/></svg>
  </div>
  <div class="abs lang"><span class="flag"></span>English
    <svg width="8" height="6" viewBox="0 0 8 6"><path d="M0 0H8L4 5Z" fill="#555"/></svg>
  </div>
  <nav class="abs nav">
    <a class="current">Home</a><a>All Products</a><a>About Us</a><a>Services</a><a>Support</a><a>Contact Us</a>
  </nav>
</header>

<section class="abs slider">
  <h1 class="abs slide-title">Plastic Distribution Box</h1>
  <p class="abs slide-text">Plastic distribution box and metal distribution box are available in Tolvirex. Distribution box is one common enclosure which used to install circuit breaker or fuse.</p>
  <div class="abs btn-dark slide-btn">READ MORE</div>
  <div class="abs slide-photo" role="img" aria-label="Group of plastic distribution boxes and enclosures"></div>
  <div class="abs dots"><span></span><span></span><span></span><span></span></div>
</section>

<section class="abs teaser" style="left:83px">
  <h3>Latest News</h3>
  <div class="thumb" role="img" aria-label="Electrician working on a panel" style="background:linear-gradient(135deg,#e9e6df,#c8a24a 60%,#2c4a8c)"></div>
  <p>Mauris vel lacus vitae felis vestibu-lum volutpat. Etiam est nunc, venenatis in, tristique eu</p>
  <div class="btn-dark">READ MORE</div>
</section>
<section class="abs teaser" style="left:324px">
  <h3>Latest Blog Post</h3>
  <div class="thumb" role="img" aria-label="AC contactor product" style="background:linear-gradient(135deg,#f2f2f2,#555)"></div>
  <p>Mauris vel lacus vitae felis vestibu-lum volutpat. Etiam est nunc, venenatis in, tristique eu</p>
  <div class="btn-dark">READ MORE</div>
</section>
<section class="abs teaser" style="left:564px">
  <h3 style="top:15px">Hot Products</h3>
  <div class="thumb" role="img" aria-label="Gears and motor components" style="top:41px;background:linear-gradient(135deg,#eee,#888)"></div>
  <p style="top:39px">Mauris vel lacus vitae felis vestibu-lum volutpat. Etiam est nunc, venenatis in, tristique eu</p>
  <div class="btn-dark">READ MORE</div>
</section>

<aside class="abs side">
  <div class="side-head">Our Products</div>
  <ul>
    <li>Vivamus porttitor</li><li>Purus nisi eleifend</li><li>Libero tempus</li><li>Libero lectus feugiat</li>
    <li>Morbi diam mauris</li><li>Gravida mattis</li><li>Morbi eget arcu</li><li>Morbi porta</li>
  </ul>
</aside>

<section class="abs recommend">
  <div class="rec-head">Recommend Product</div>
  <div class="rec-grid">
    <div class="product"><div class="pic" role="img" aria-label="Push button switch"></div><h4>Product Name</h4><p>vitae felis vestibulum volut-pat Etiam Morbi eget arcu lectus feugiat</p><div class="btn-red">READ MORE</div></div>
    <div class="product"><div class="pic" role="img" aria-label="Red push button"></div><h4>Product Name</h4><p>vitae felis vestibulum volut-pat Etiam Morbi eget arcu lectus feugiat</p><div class="btn-red">READ MORE</div></div>
    <div class="product"><div class="pic" role="img" aria-label="Emergency stop button"></div><h4>Product Name</h4><p>vitae felis vestibulum volut-pat Etiam Morbi eget arcu lectus feugiat</p><div class="btn-red">READ MORE</div></div>
    <div class="product"><div class="pic" role="img" aria-label="Wall switch"></div><h4>Product Name</h4><p>vitae felis vestibulum volut-pat Etiam Morbi eget arcu lectus feugiat</p><div class="btn-red">READ MORE</div></div>
  </div>
</section>

<section class="abs about">
  <h2>About Our Company</h2>
  <p>Tolvirex Electric Enterprises is one of specialized manufacturers and exporters in line of low, middle and high voltage electric equipments. More than 15 years manufacture and export experience, technology and quality of products and our service win high reputation from the old and new customers around the world, 12 countries sole agents has signed successfully, another creating branch company in Lima, Peru and Lattakia, Syria.</p>
  <p>Phasellus felis dolor, scelerisque a, tempus eget, lobortis id, libero. Donec scelerisque leo ac risus. Praesent sit amet est. In dictum, dolor eu dictum porttitor, enim felis viverra mi, eget luctus massa purus quis odio.</p>
</section>

<aside class="abs chat">
  <div class="photo" role="img" aria-label="Smiling support agent giving thumbs up"></div>
  <h3>Live Chat<br>Online Exchange</h3>
  <p>Lorem ipsum dolor sit amet, consectetuer adipiscing elit.</p>
  <div class="btn-dark">GET NOW</div>
</aside>

<footer class="abs footer">
  <div class="fcol" style="left:84px;width:103px"><h5>All Products</h5><ul><li>All Products</li><li>What's New</li><li>Recommend Products</li><li>Download Products</li></ul></div>
  <div class="fcol" style="left:208px;width:76px"><h5>About Us</h5><ul><li>About Us</li><li>Latest News</li><li>Advantages</li><li>Certification</li></ul></div>
  <div class="fcol" style="left:305px;width:104px"><h5>Services</h5><ul><li>Site Map</li><li>Web Links</li><li>Privacy Policy</li><li>Terms and Conditions</li></ul></div>
  <div class="fcol" style="left:431px;width:114px"><h5>Contact Us</h5><ul><li>Tel: 0086-571-40215530</li><li>Fax: 0086-571-40215531</li><li>M.B: 0086-13988104726</li><li>Skype: tolvirex2008</li></ul></div>
  <div class="fcol" style="left:562px;width:101px"><h5>Online Support</h5><ul><li><span class="skype"></span>tolvirexcn</li><li><span class="skype"></span>tolvirexchina</li><li><span class="skype"></span>tolvirexelectric</li><li><span class="skype"></span>tolvirex2008</li></ul></div>
  <div class="fcol" style="left:682px;top:26px;border:0"><h5>Get Connected</h5>
    <div class="social"><span style="background:#3b5998"></span><span style="background:#33aaf3"></span><span style="background:#0e76a8"></span><span style="background:#3d7ce8"></span><span style="background:#cb2027"></span></div>
  </div>
</footer>
<div class="abs copyright">© 2013 Company Name. All right reserved. Term of Use</div>
</body>
</html>
```